Business Card Project for Firm Deck Hoisting

Business name is "Firm Deck Hoisting" we are a scaffolding & rigging business specialising in local and remote work for:
- scaffolding (residential, commercial, industrial)
- rigging
-man material hoists
- swing stages
- labour hire

On the back of the card I would like FDH as the symbol / logo. I have attached the logos we have had created by sketch harbour. We would like to use bold colours – preferably as the same colour scheme as the logo.

Target Market(s)

Construction business

Industry/Entity Type

Construction

Contact Information for Business Card

name: Owen Pellew
Title: Director
Phone: 0491 572 864
Address: PO BOX 3251, Tarrinby SA 5163
Email: owen@firmdeckhoisting.com.au
Website: www.firmdeckhoisting.com.au

Font styles to use
Sans Serif

Requirements
Must have
• Must use existing logo & prefering using bold colours
Nice to have
• Would be nice to have a line of dot points in what we specialise in but not essential
• Would be nice to see some designs with a slogan but not essential
Should not have
• NA

```html
<!DOCTYPE html>
<html lang="en">
<head>
<meta charset="utf-8">
<title>Firm Deck Hoisting – Business Card</title>
<link rel="stylesheet" href="https://fonts.googleapis.com/css2?family=Michroma&family=Source+Sans+3:wght@400&display=swap">
<style>
  :root {
    --stage: #6d6d6d;
    --card-light: #f3f3f3;
    --card-dark: #231f20;
    --ink: #231f20;
    --red: #e3262b;
    --white: #ffffff;
  }
  * { margin: 0; padding: 0; box-sizing: border-box; }
  html, body {
    width: 1200px; height: 900px; overflow: hidden;
    background: var(--stage);
  }
  .canvas { position: relative; width: 1200px; height: 900px; }

  .card { position: absolute; top: 200px; width: 310px; height: 502px; }
  .card--front {
    left: 301px; background: var(--card-light);
    border-radius: 62px 0 62px 0;
    color: var(--ink);
  }
  .card--back {
    left: 641px; width: 309px; background: var(--card-dark);
    border-radius: 0 62px 0 62px;
    color: var(--white);
  }

  .brand {
    position: absolute; left: 0; right: 0;
    display: flex; align-items: center; justify-content: center; gap: 10px;
    font-family: "Michroma", sans-serif;
    font-size: 15px; letter-spacing: 0.5px; line-height: 1;
    white-space: nowrap;
  }
  .brand__square { width: 26px; height: 26px; background: var(--red); flex: none; }
  .card--front .brand { top: 113px; color: var(--ink); }
  .card--back .brand { top: 125px; color: var(--white); }

  .person { position: absolute; left: 26px; top: 213px; font-family: "Michroma", sans-serif; }
  .person__name { font-size: 16.5px; letter-spacing: 0.7px; line-height: 1; }
  .person__surname { color: var(--red); }
  .person__title { margin-top: 8px; font-size: 12.5px; letter-spacing: 0.5px; }

  .contact {
    position: absolute; left: 27px; top: 301px; list-style: none;
    font-family: "Source Sans 3", sans-serif; font-size: 15.5px; line-height: 19px;
  }
  .contact li { display: flex; align-items: center; gap: 6px; }
  .contact svg { width: 9px; height: 9px; fill: var(--red); flex: none; }

  .address {
    position: absolute; left: 0; right: 0; top: 403px; text-align: center;
    font-family: "Michroma", sans-serif; font-size: 10px; letter-spacing: 0.2px;
    white-space: nowrap;
  }

  .services {
    position: absolute; left: 0; right: 0; top: 244px; list-style: none;
    text-align: center;
    font-family: "Michroma", sans-serif; font-size: 14.8px; letter-spacing: 0.6px;
    line-height: 30px; white-space: nowrap;
  }
</style>
</head>
<body>
<main class="canvas">
  <section class="card card--front" aria-label="Card front">
    <div class="brand"><span class="brand__square"></span><span class="brand__name">FIRM DECK HOISTING</span></div>

    <div class="person">
      <p class="person__name">OWEN <span class="person__surname">PELLEW</span></p>
      <p class="person__title">DIRECTOR</p>
    </div>

    <ul class="contact">
      <li><svg viewBox="0 0 10 10" aria-hidden="true"><path d="M2.5 0h5a1 1 0 0 1 1 1v8a1 1 0 0 1-1 1h-5a1 1 0 0 1-1-1V1a1 1 0 0 1 1-1zm.6 1.4v6h3.8v-6zM5 8a.6.6 0 1 0 0 1.2A.6.6 0 0 0 5 8z"/></svg>0491 572 864</li>
      <li><svg viewBox="0 0 10 10" aria-hidden="true"><path d="M0 2h10v6H0zm.8.6L5 5.6l4.2-3z"/></svg>owen@firmdeckhoisting.com.au</li>
      <li><svg viewBox="0 0 10 10" aria-hidden="true"><circle cx="5" cy="5" r="5"/></svg>www.firmdeckhoisting.com.au</li>
    </ul>

    <p class="address">PO BOX 3251, TARRINBY SA 5163</p>
  </section>

  <section class="card card--back" aria-label="Card back">
    <div class="brand"><span class="brand__square"></span><span class="brand__name">FIRM DECK HOISTING</span></div>

    <ul class="services">
      <li>SCAFFOLDING</li>
      <li>RIGGING</li>
      <li>MAN MATERIAL HOISTS</li>
      <li>SWING STAGES</li>
      <li>LABOUR HIRE</li>
    </ul>
  </section>
</main>
</body>
</html>
```